Harbor Glow Living.com Landing Page

Create a well designed home/landing page using that communicates the feeling of Harbor Glow Living with this sections that scroll from top to bottom -
Top section - Displays "Harbor Glow Living" with space for embedded YouTube video.

The following sections follow the top section -
Assess your current Harbor Glow Living. Complete our free life balance assessment to identify key areas where you you will most benefit.
"Learn more" call to action button

Create a Harbor Glow Living Study Hub account. Get a 14 day free trial to a wealth of learning activities, motivational videos and professional presentations on our learning portal designed specifically to address the eight essential areas of Harbor Glow Living.
"Register now" call to action button

Get weekly reports on your progress and goal achievement. Celebrate your success each week as you review your progress on each life balance area.

Appropriate royalty free photos and graphics that fit the chosen theme you recommend.
Updates

I'm reviewing the designs. I realize that I need to clarify that Harbor Glow Living focuses on eight areas, not just physical fitness and meditation. Spirituality and Sense of Purpose; Fitness and Health; Relationships; Personal Finance; Recreation and Fun; Physical Environment; Personal Development and Learning; Work and Career

Number of Pages Required

1 page

Colors
33a6d7
00a990
9bcb3c
2f73b3

```html
<!DOCTYPE html>
<html lang="en">
<head>
<meta charset="utf-8">
<title>Harbor Glow Living</title>
<link rel="stylesheet" href="https://fonts.googleapis.com/css2?family=Domine:wght@400;700&family=Oswald:wght@700&display=swap">
<style>
  :root {
    --sky-blue: #33a6d7;
    --teal: #00a990;
    --lime: #9bcb3c;
    --ocean: #2f73b3;
    --white: #ffffff;
    --ink: #2b2b2b;
  }
  * { margin: 0; padding: 0; box-sizing: border-box; }
  html, body { width: 1200px; height: 2440px; overflow: hidden; background: var(--white); }
  body { font-family: "Domine", Georgia, serif; color: var(--white); }
  .page { position: relative; width: 1200px; height: 2440px; }

  .hero { position: absolute; left: 0; top: 0; width: 1200px; height: 635px; }
  .hero__photo { position: absolute; inset: 0; }
  .hero__title {
    position: absolute; top: 42px; left: 0; width: 100%;
    text-align: center; font-family: "Oswald", "Arial Narrow", sans-serif;
    font-weight: 700; font-size: 64px; line-height: 72px; color: var(--teal);
  }
  .hero__play { position: absolute; left: 542px; top: 252px; width: 116px; height: 116px; }

  .feature { position: absolute; left: 0; width: 1200px; height: 568px; }
  .feature__art { position: absolute; inset: 0; }
  .feature--assess { top: 635px; }
  .feature--portal { top: 1203px; }
  .feature--reports { top: 1771px; height: 570px; }

  .feature__heading { position: absolute; font-weight: 700; }
  .feature__body { position: absolute; font-weight: 400; }
  .cta {
    position: absolute; display: block; width: 175px; height: 48px;
    border: 3px solid var(--white); text-align: center; line-height: 42px;
    font-size: 14px; font-weight: 700; letter-spacing: 0.3px; color: var(--white);
    text-decoration: none; text-transform: uppercase;
  }

  .feature--assess .feature__heading { left: 677px; top: 198px; font-size: 35px; line-height: 42px; }
  .feature--assess .feature__body { left: 678px; top: 300px; width: 400px; font-size: 21px; line-height: 27px; }
  .feature--assess .cta { left: 690px; top: 404px; }

  .feature--portal .feature__heading { left: 86px; top: 160px; font-size: 28px; line-height: 33px; }
  .feature--portal .feature__offer { position: absolute; left: 89px; top: 233px; font-size: 42px; line-height: 50px; font-weight: 700; }
  .feature--portal .feature__body { left: 87px; top: 296px; width: 490px; font-size: 17px; line-height: 21px; }
  .feature--portal .cta { left: 89px; top: 398px; }

  .feature--reports .feature__heading { left: 647px; top: 196px; width: 450px; font-size: 35px; line-height: 41px; }
  .feature--reports .feature__body { left: 647px; top: 336px; width: 360px; font-size: 19px; line-height: 23px; }
  .feature--reports .cta { left: 647px; top: 418px; }

  .footer {
    position: absolute; left: 0; top: 2341px; width: 1200px; height: 99px;
    text-align: center; padding-top: 44px; font-size: 15px; color: var(--ink);
  }
</style>
</head>
<body>
<main class="page">

  <header class="hero">
    <svg class="hero__photo" viewBox="0 0 1200 635" preserveAspectRatio="none" role="img" aria-label="Photo: woman seated cross-legged on a wooden deck, arms raised in a yoga pose, facing misty blue mountains">
      <defs>
        <linearGradient id="heroSky" x1="0" y1="0" x2="0" y2="1">
          <stop offset="0" stop-color="#d8eef8"/>
          <stop offset="0.45" stop-color="#a9d3e8"/>
          <stop offset="0.65" stop-color="#4f93ad"/>
          <stop offset="0.9" stop-color="#2e6f68"/>
          <stop offset="1" stop-color="#8a8b86"/>
        </linearGradient>
      </defs>
      <rect width="1200" height="635" fill="url(#heroSky)"/>
    </svg>
    <h1 class="hero__title">Harbor Glow Living</h1>
    <svg class="hero__play" viewBox="0 0 116 116" aria-label="Play video">
      <defs>
        <linearGradient id="playRing" x1="0" y1="0" x2="1" y2="1">
          <stop offset="0" stop-color="#33a6d7"/>
          <stop offset="0.55" stop-color="#00a990"/>
          <stop offset="1" stop-color="#9bcb3c"/>
        </linearGradient>
      </defs>
      <circle cx="58" cy="58" r="58" fill="url(#playRing)"/>
      <circle cx="58" cy="58" r="44" fill="none" stroke="#ffffff" stroke-width="3"/>
      <path d="M49 40 L75 58 L49 76 Z" fill="#ffffff"/>
    </svg>
  </header>

  <section class="feature feature--assess">
    <svg class="feature__art" viewBox="0 0 1200 568" preserveAspectRatio="none">
      <defs>
        <linearGradient id="lakePhoto" x1="0" y1="0" x2="0" y2="1">
          <stop offset="0" stop-color="#b9dde4"/>
          <stop offset="0.3" stop-color="#3f8a74"/>
          <stop offset="0.55" stop-color="#7fa7a5"/>
          <stop offset="1" stop-color="#8b8177"/>
        </linearGradient>
      </defs>
      <rect width="640" height="568" fill="url(#lakePhoto)" role="img" aria-label="Photo: young woman meditating on a lakeside dock beside forested hills"/>
      <polygon points="528,0 1200,0 1200,568 624,568" fill="var(--teal)"/>
    </svg>
    <h2 class="feature__heading">Assess your current<br>Harbor Glow Living.</h2>
    <p class="feature__body">Complete our free life balance assessment to identify key areas where you you will most benefit.</p>
    <a class="cta" href="#assess">Learn more</a>
  </section>

  <section class="feature feature--portal">
    <svg class="feature__art" viewBox="0 0 1200 568" preserveAspectRatio="none">
      <defs>
        <linearGradient id="sunsetPhoto" x1="0" y1="0" x2="1" y2="1">
          <stop offset="0" stop-color="#f2c98a"/>
          <stop offset="0.4" stop-color="#f6e3c2"/>
          <stop offset="0.7" stop-color="#e9c9cf"/>
          <stop offset="1" stop-color="#9ec8dd"/>
        </linearGradient>
      </defs>
      <rect x="540" width="660" height="568" fill="url(#sunsetPhoto)" role="img" aria-label="Photo: woman in a white dress raising her arms toward a pastel sunset sky"/>
      <polygon points="0,0 624,0 554,568 0,568" fill="var(--ocean)"/>
    </svg>
    <h2 class="feature__heading">Create a Harbor Glow Living<br>Study Hub account.</h2>
    <p class="feature__offer">Get a 14 day free trial</p>
    <p class="feature__body">to a wealth of learning activities, motivational videos and professional presentations on our learning portal designed specifically to address the eight essential areas of Harbor Glow Living.</p>
    <a class="cta" href="#register">Register now</a>
  </section>

  <section class="feature feature--reports">
    <svg class="feature__art" viewBox="0 0 1200 570" preserveAspectRatio="none">
      <defs>
        <linearGradient id="runnerPhoto" x1="0" y1="0" x2="1" y2="1">
          <stop offset="0" stop-color="#e9e6e1"/>
          <stop offset="0.35" stop-color="#b88a6a"/>
          <stop offset="0.6" stop-color="#d4576f"/>
          <stop offset="1" stop-color="#8f7f76"/>
        </linearGradient>
      </defs>
      <rect width="620" height="570" fill="url(#runnerPhoto)" role="img" aria-label="Photo: smiling woman in a pink shirt jogging outdoors at golden hour"/>
      <polygon points="554,0 1200,0 1200,570 603,570" fill="var(--lime)"/>
    </svg>
    <h2 class="feature__heading">Get weekly reports on your progress and goal achievement.</h2>
    <p class="feature__body">Celebrate your success each week as you review your progress on each life balance area.</p>
    <a class="cta" href="#reports">Learn more</a>
  </section>

  <footer class="footer">Copyright 2020 Harbor Glow Living.com All Rights Reserved</footer>

</main>
</body>
</html>
```